Working Capital graphics

Our business advisory firm requires 9 images to be re-created and improved in the branding of our business.

The 9 images have been uploaded below and the colours and branding of the business can be found at the website www.dunmorrowadvisory.com.au

```html
<!DOCTYPE html>
<html lang="en">
<head>
<meta charset="utf-8">
<title>Net working capital absorption</title>
<link href="https://fonts.googleapis.com/css2?family=Montserrat:ital,wght@0,400;0,500;1,800&display=swap" rel="stylesheet">
<style>
  :root {
    --brand-ink: #111111;
    --brand-red: #ED2228;
    --brand-orange: #F09C43;
    --brand-paper: #ffffff;
  }
  html, body {
    margin: 0;
    padding: 0;
    background: var(--brand-paper);
    overflow: hidden;
  }
  .canvas {
    width: 1200px;
    height: 1000px;
    position: relative;
    overflow: hidden;
    background: var(--brand-paper);
    font-family: "Montserrat", "Helvetica Neue", Arial, sans-serif;
  }
  .chart { display: block; }
  .chart-title {
    font-weight: 800;
    font-style: italic;
    font-size: 39px;
    fill: var(--brand-ink);
  }
  .axis-line { stroke: var(--brand-ink); stroke-width: 3; fill: none; }
  .tick-label { font-size: 28px; font-weight: 500; fill: var(--brand-ink); }
  .axis-title { font-size: 29px; font-weight: 400; fill: var(--brand-ink); }
  .axis-title--sales { font-size: 31px; }
  .zone { fill: var(--brand-orange); }
  .guide { stroke: var(--brand-red); stroke-width: 2.5; stroke-dasharray: 10 7; fill: none; }
  .vector { stroke: var(--brand-red); stroke-width: 3; fill: none; }
  .arrow-head { fill: var(--brand-red); }
  .origin { fill: var(--brand-red); }
  .vector-letter { font-size: 33px; font-weight: 500; fill: var(--brand-ink); }
  .vector-name { font-size: 28px; font-weight: 500; fill: var(--brand-ink); }
</style>
</head>
<body>
<main class="canvas">
  <svg class="chart" width="1200" height="1000" viewBox="0 0 1200 1000" role="img" aria-label="Net working capital absorption chart: sales versus net working capital with six movement directions">
    <defs>
      <marker id="arrowhead" viewBox="0 0 12 12" refX="10" refY="6" markerWidth="5" markerHeight="5" orient="auto-start-reverse" markerUnits="strokeWidth">
        <path class="arrow-head" d="M0,0 L12,6 L0,12 L3,6 Z"/>
      </marker>
    </defs>

    <text class="chart-title" x="185" y="104">Net working capital absorption</text>

    <!-- Risk zone -->
    <path class="zone" d="M616,480 L616,272 A208,208 0 1,0 832,480 Z"/>

    <!-- Axes -->
    <line class="axis-line" x1="287" y1="148" x2="287" y2="824"/>
    <line class="axis-line" x1="286" y1="823" x2="952" y2="823"/>

    <!-- Y axis ticks -->
    <g class="y-ticks" text-anchor="end">
      <text class="tick-label" x="263" y="178">450m</text>
      <text class="tick-label" x="263" y="267">400m</text>
      <text class="tick-label" x="263" y="355">350m</text>
      <text class="tick-label" x="263" y="443">300m</text>
      <text class="tick-label" x="263" y="530">250m</text>
      <text class="tick-label" x="263" y="618">200m</text>
      <text class="tick-label" x="263" y="707">150m</text>
    </g>
    <text class="axis-title axis-title--sales" transform="translate(157,483) rotate(-90)" text-anchor="middle">Sales</text>

    <!-- X axis ticks -->
    <g class="x-ticks" text-anchor="middle">
      <text class="tick-label" x="343" y="867">20m</text>
      <text class="tick-label" x="449" y="867">25m</text>
      <text class="tick-label" x="556" y="867">30m</text>
      <text class="tick-label" x="663" y="867">35m</text>
      <text class="tick-label" x="770" y="867">40m</text>
      <text class="tick-label" x="877" y="867">45m</text>
    </g>
    <text class="axis-title" x="620" y="916" text-anchor="middle">Net Working Capital (NWC)</text>

    <!-- Reference guides -->
    <line class="guide" x1="287" y1="480" x2="623" y2="480"/>
    <line class="guide" x1="624" y1="480" x2="624" y2="823"/>

    <!-- Movement vectors -->
    <g class="vectors">
      <line class="vector" x1="624" y1="480" x2="459" y2="305" marker-end="url(#arrowhead)"/>
      <line class="vector" x1="624" y1="480" x2="624" y2="212" marker-end="url(#arrowhead)"/>
      <line class="vector" x1="624" y1="480" x2="766" y2="268" marker-end="url(#arrowhead)"/>
      <line class="vector" x1="624" y1="480" x2="878" y2="480" marker-end="url(#arrowhead)"/>
      <line class="vector" x1="624" y1="480" x2="776" y2="658" marker-end="url(#arrowhead)"/>
      <line class="vector" x1="624" y1="480" x2="426" y2="640" marker-end="url(#arrowhead)"/>
    </g>
    <circle class="origin" cx="624" cy="480" r="17"/>

    <!-- Vector labels -->
    <text class="vector-name" x="328" y="241">Optimal growth</text>
    <text class="vector-letter" x="428" y="290">A</text>
    <text class="vector-letter" x="620" y="192">B</text>
    <text class="vector-letter" x="762" y="252">C</text>
    <text class="vector-name" x="808" y="253">Fast growth</text>
    <text class="vector-letter" x="866" y="464">D</text>
    <text class="vector-name" x="915" y="441">Declining</text>
    <text class="vector-name" x="915" y="468">growth</text>
    <text class="vector-letter" x="794" y="671">E</text>
    <text class="vector-name" x="840" y="670">Corporate stress</text>
    <text class="vector-letter" x="395" y="671">F</text>
    <text class="vector-name" x="393" y="718">Downsizing</text>
  </svg>
</main>
</body>
</html>
```